Upsell Vertical Banner Ad Design For B2B Marketing Agency Vertical 768px × 1180px IS THE SIZE

I need a banner made for my website www.brightharborgrowthworks.biz This banner will be an upsell advertisement for after someone signs up for my monthly program. When they login to their account for the 1st time I will give them the chance to upgrade their account to our annual program with just one click.

this is a page that upsells it currently to give you an idea how we market ourselves:
https://bhgw.pagevault-example.com/page/bhg-annual-upsell

Use this content:

Are You Ready To Commit To Taking Your Business To The Next Level?

Because We're In This For The Long-Haul and Dedicated To Your Success...

Save $300 By Upgrading To An Annual Membership And Pay Only $74/mth

((BUTTON))Yes, Upgrade My Plan Right Now!

*Must prepay the full year at only $898/yr!

Target Market(s)

business owners

Industry/Entity Type

Marketing

Requirements
Must have
• 768px × 1180px IS THE SIZE vertical

Use this content:

Nice to have
• Use this content:

Should not have
• Use this content:

```html
<!DOCTYPE html>
<html lang="en">
<head>
<meta charset="utf-8">
<title>Annual Membership Upgrade</title>
<link rel="stylesheet" href="https://fonts.googleapis.com/css2?family=Montserrat:wght@300;400;800&display=swap">
<style>
  :root {
    --brand-blue: #1074bd;
    --button-blue: #1170b8;
    --paper: #ebe7e8;
    --ink: #111111;
    --white: #ffffff;
  }
  html, body {
    margin: 0;
    padding: 0;
    width: 781px;
    height: 1200px;
    overflow: hidden;
    background: var(--paper);
  }
  .banner {
    position: relative;
    width: 768px;
    height: 1180px;
    background: var(--paper);
    transform: scale(1.01693);
    transform-origin: 0 0;
    overflow: hidden;
    font-family: "Montserrat", sans-serif;
    color: var(--ink);
  }
  .banner__arc {
    position: absolute;
    left: 0;
    top: 0;
  }
  .hero {
    position: absolute;
    left: 0;
    top: 39px;
    width: 768px;
    text-align: center;
    color: var(--white);
  }
  .hero__title {
    margin: 0;
    font-weight: 800;
    font-size: 31.5px;
    line-height: 44px;
    letter-spacing: 0.1px;
  }
  .hero__subtitle {
    margin: 10px 0 0;
    font-weight: 400;
    font-size: 19.5px;
    line-height: 27px;
    letter-spacing: 0.4px;
  }
  .offer {
    position: absolute;
    left: 0;
    top: 576px;
    width: 768px;
    text-align: center;
  }
  .offer__headline {
    margin: 0;
    font-weight: 300;
    font-size: 39px;
    line-height: 48px;
    letter-spacing: 0.6px;
  }
  .offer__detail {
    margin: 7px 0 0;
    font-weight: 400;
    font-size: 18.4px;
    line-height: 24px;
    letter-spacing: 0.3px;
  }
  .cta {
    position: absolute;
    left: 162px;
    top: 938px;
    width: 444px;
    height: 61px;
    border-radius: 4px;
    background: var(--button-blue);
    color: var(--white);
    font-family: "Montserrat", sans-serif;
    font-weight: 300;
    font-size: 24.3px;
    line-height: 61px;
    text-align: center;
    text-decoration: none;
    letter-spacing: 0.3px;
  }
  .footnote {
    position: absolute;
    left: 0;
    top: 1013px;
    width: 768px;
    margin: 0;
    text-align: center;
    font-weight: 400;
    font-size: 16.5px;
    line-height: 22px;
  }
  .brand {
    position: absolute;
    left: 0;
    top: 1093px;
    width: 768px;
    height: 38px;
    display: flex;
    justify-content: center;
    align-items: center;
    gap: 10px;
  }
  .brand__mark {
    width: 38px;
    height: 38px;
    background: var(--brand-blue);
  }
  .brand__name {
    font-weight: 800;
    font-size: 15.5px;
    letter-spacing: 0.8px;
    color: var(--brand-blue);
    text-transform: uppercase;
  }
</style>
</head>
<body>
  <main class="banner">
    <svg class="banner__arc" width="768" height="320" viewBox="0 0 768 320" aria-hidden="true">
      <ellipse cx="390" cy="-60" rx="462" ry="366" fill="var(--brand-blue)"/>
    </svg>

    <header class="hero">
      <h1 class="hero__title">Are You Ready<br>To Commit To Taking Your Business<br>To The Next Level?</h1>
      <p class="hero__subtitle">Because We're In This For The Long-Haul<br>and Dedicated To Your Success...</p>
    </header>

    <section class="offer">
      <h2 class="offer__headline">Save $300</h2>
      <p class="offer__detail">By Upgrading To An Annual Membership And Pay Only $74/mth.</p>
    </section>

    <a class="cta" href="#upgrade">Yes, Upgrade My Plan Right Now!</a>
    <p class="footnote">*Must prepay the full year at only $898/yr!</p>

    <footer class="brand">
      <span class="brand__mark" aria-hidden="true"></span>
      <span class="brand__name">Bright Harbor Growth Works</span>
    </footer>
  </main>
</body>
</html>
```